Business Card & Letterhead Design

We a financial advice company based in Australia. We provide advice to wealthy farmers.

We are changing our business name FROM Brightmere Financial TO Calderstone Wealth and we need a new letterhead and double sided business card design

Attached is designs from our previous branding (Brightmere Financial) as it includes all the details we require on the new Calderstone Wealth business cards and letterhead.

```html
<!DOCTYPE html>
<html lang="en">
<head>
<meta charset="utf-8">
<title>Calderstone Wealth Letterhead</title>
<link href="https://fonts.googleapis.com/css2?family=Lato:wght@400;700&display=swap" rel="stylesheet">
<style>
  :root {
    --slate: #5c6870;
    --paper: #ffffff;
    --ink: #2b2b2b;
    --on-slate: #f2f4f5;
    --watermark: #e0e0e0;
  }
  * { margin: 0; padding: 0; box-sizing: border-box; }
  html, body { width: 1200px; height: 1000px; overflow: hidden; background: var(--paper); }
  body { font-family: 'Lato', sans-serif; color: var(--ink); position: relative; }

  .letterhead { position: absolute; left: 245px; top: 0; width: 713px; height: 1000px; background: var(--paper); }

  .header-band { position: absolute; left: 0; top: 0; width: 713px; height: 157px; background: var(--slate); color: var(--on-slate); }

  .brand { position: absolute; left: 40px; top: 40px; width: 232px; text-align: center; }
  .brand-mark { display: block; margin: 0 auto 6px; }
  .brand-name { font-size: 21px; letter-spacing: 1.2px; text-transform: uppercase; font-weight: 400; line-height: 1; white-space: nowrap; }
  .brand-tagline { font-size: 8.5px; letter-spacing: 3.1px; text-transform: uppercase; margin-top: 3px; white-space: nowrap; }

  .divider { position: absolute; top: 35px; width: 1px; height: 103px; background: var(--on-slate); opacity: .85; }
  .divider-one { left: 302px; }
  .divider-two { left: 476px; }

  .entity-details { position: absolute; top: 33px; font-size: 11px; line-height: 15.2px; white-space: nowrap; }
  .entity-representative { left: 322px; }
  .entity-licensee { left: 497px; top: 40px; }

  .watermark { position: absolute; left: 93px; top: 254px; }

  .footer-contact { position: absolute; top: 874px; font-size: 11px; line-height: 14.2px; white-space: nowrap; }
  .contact-address { left: 133px; }
  .contact-lines { left: 427px; }

  .footer-band { position: absolute; left: 0; top: 937px; width: 713px; height: 63px; background: var(--slate); color: var(--on-slate); display: flex; align-items: center; justify-content: center; padding-bottom: 4px; }
  .footer-slogan { font-size: 17px; font-weight: 700; letter-spacing: .2px; }
</style>
</head>
<body>
  <main class="letterhead">
    <header class="header-band">
      <div class="brand">
        <svg class="brand-mark" width="44" height="44" viewBox="0 0 44 44" aria-hidden="true">
          <circle cx="22" cy="22" r="20" fill="none" stroke="#f2f4f5" stroke-width="2"/>
        </svg>
        <div class="brand-name">Calderstone Wealth</div>
        <div class="brand-tagline">Strategic Financial Advice</div>
      </div>

      <span class="divider divider-one"></span>
      <div class="entity-details entity-representative">
        Wexford Holdings Pty Ltd<br>
        ATF The Ashgrove Investment<br>
        Trust T/AS Brightmere Financial<br>
        ABN: 48 205 316 927<br>
        Corporate Authorised<br>
        Representative of Meridian<br>
        Advice Partners Limited
      </div>

      <span class="divider divider-two"></span>
      <div class="entity-details entity-licensee">
        Meridian Advice Partners Limited<br>
        ABN 61 004 812 357<br>
        Australian Financial Services Licence<br>
        Licence Number 318 442<br>
        Principle Address: 410 Harbour St<br>
        PO Box 4512 Melbourne VIC 3001
      </div>
    </header>

    <svg class="watermark" width="528" height="528" viewBox="0 0 528 528" aria-hidden="true">
      <circle cx="264" cy="264" r="257" fill="none" stroke="var(--watermark)" stroke-width="12"/>
    </svg>

    <address class="footer-contact contact-address" style="font-style:normal">
      Suite 7A, 18 Renwick St<br>
      Kangaroo Point QLD 4169<br>
      PO Box 5204<br>
      East Brisbane QLD 4169
    </address>
    <div class="footer-contact contact-lines">
      p (07) 3000 1842<br>
      f (07) 3000 1843<br>
      www.brightmerefinancial.com.au<br>
      admin@brightmerefinancial.com.au
    </div>

    <footer class="footer-band">
      <p class="footer-slogan">'Financial peace of mind'</p>
    </footer>
  </main>
</body>
</html>
```